Lantern over the Harbor ~ A Widening Passage for Writers

My book is called “Lantern over the Harbor.” Its subtitle is “A Widening Passage for Writers.” It is a book about being a poet, writing poetry, and the ways in which poets are connected to both society and the central energy of the Universe. I want the cover design to be abstract and impressionistic. A suggestion of fireworks or a starburst would be a plus. To be consistent with the 3 other books I have published, I want the font for the title, as well as my name (Dorothea Quillbrake) to be Papyrus. The subtitle font can be something more plain and sans serif, like Arial or Franklin Gothic Book, probably in italics. As for color, I definitely want pale gold (angelic). Possible other complimentary colors could be either light or dark shades of gray, turquoise, rose, rust or red. I'm attaching the back cover text and also three pages from inside the book that have line drawings, to give an example of the interior artwork.
Updates

Forgot to mention: My book is a paperback. Its size will be 8.5" high and 5.5" wide. I'm self-publishing it, and it will be printed by Halvern Printworks in Nebraska, USA. It has 104 pages. I think you need the number of pages, in order to make the spine of the book the correct width.

Target Market(s)

My target market is people who write poetry or are interested in how poetry is written.

Industry/Entity Type

Poetry

Font styles to use
Sans Serif
Other font styles liked:
• Papyrus for the front cover. Arial or another sans serif font on the back cover.

Colors

Designer to choose colors to be used in the design.

Requirements
Must have
• My book cover needs to be inspiring and uplifting, as well as abstract and impressionistic, with kind of a "New Age" feel. I don't want anything that looks rigid and scholarly.
Nice to have
• The book talks about the connection poets have to the Universe and the Creative Energy at the center of everything. The cover should convey that Energy.
Should not have
• My cover should not be realistic, logical or straight-laced. I want something that feels free, imaginative and unfettered.

```html
<!DOCTYPE html>
<html lang="en">
<head>
<meta charset="utf-8">
<title>Lantern over the Harbor — Book Cover</title>
<link href="https://fonts.googleapis.com/css2?family=Macondo&family=Questrial&display=swap" rel="stylesheet">
<style>
  :root {
    --stage: #2f2f2f;
    --teal-light: #5f8a8b;
    --teal-mid: #426d70;
    --teal-dark: #2a4f53;
    --teal-deep: #1f3f43;
    --cream: #f3e6cc;
    --pale-gold: #e2c79a;
    --gold: #c9a673;
    --tan: #a8825a;
    --ink-light: #f4ead6;
  }
  * { margin: 0; padding: 0; box-sizing: border-box; }
  html, body {
    width: 1200px;
    height: 1200px;
    overflow: hidden;
    background: var(--stage);
  }
  .stage {
    width: 1200px;
    height: 1200px;
    display: flex;
    align-items: center;
    justify-content: center;
  }
  .book-cover {
    position: relative;
    width: 680px;
    height: 1050px;
    overflow: hidden;
    background: radial-gradient(ellipse at 45% 48%, var(--teal-light) 0%, var(--teal-mid) 45%, var(--teal-dark) 85%, var(--teal-deep) 100%);
    box-shadow: 0 10px 40px rgba(0,0,0,0.45);
  }
  .corner-band {
    position: absolute;
    inset: 0;
    width: 100%;
    height: 100%;
  }
  .cover-illustration {
    position: absolute;
    left: 50px;
    top: 200px;
    width: 500px;
    height: 500px;
    border-radius: 50%;
    background: radial-gradient(ellipse at 55% 45%, rgba(236, 214, 170, 0.5) 0%, rgba(226, 199, 154, 0.25) 42%, rgba(226, 199, 154, 0) 72%);
  }
  .title-block {
    position: absolute;
    right: 28px;
    top: 548px;
    width: 440px;
    color: var(--ink-light);
  }
  .book-title {
    font-family: "Macondo", Papyrus, fantasy;
    font-weight: 400;
    font-size: 76px;
    line-height: 1.02;
    text-align: right;
    letter-spacing: 0.5px;
  }
  .book-subtitle {
    margin-top: 16px;
    font-family: "Questrial", Arial, sans-serif;
    font-style: italic;
    font-size: 21px;
    text-align: center;
    padding-left: 50px;
    letter-spacing: 0.3px;
  }
  .book-author {
    margin-top: 6px;
    font-family: "Macondo", Papyrus, fantasy;
    font-size: 32px;
    text-align: center;
    padding-left: 50px;
  }
</style>
</head>
<body>
  <main class="stage">
    <section class="book-cover">
      <svg class="corner-band" viewBox="0 0 680 1050" preserveAspectRatio="none">
        <defs>
          <linearGradient id="band-top" x1="0" y1="0" x2="1" y2="1">
            <stop offset="0" stop-color="var(--cream)"/>
            <stop offset="0.6" stop-color="var(--pale-gold)"/>
            <stop offset="1" stop-color="var(--gold)"/>
          </linearGradient>
          <linearGradient id="band-bottom" x1="1" y1="1" x2="0" y2="0">
            <stop offset="0" stop-color="var(--cream)"/>
            <stop offset="0.6" stop-color="var(--pale-gold)"/>
            <stop offset="1" stop-color="var(--gold)"/>
          </linearGradient>
        </defs>
        <path role="img" aria-label="Layered wavy bands of cream and pale gold sweeping across the top left corner" fill="url(#band-top)" d="M0 0 H680 C560 110 420 170 300 250 C200 315 100 340 0 400 Z"/>
        <path role="img" aria-label="Layered wavy bands of cream and pale gold sweeping across the bottom right corner" fill="url(#band-bottom)" d="M680 1050 H0 C120 1010 260 990 400 930 C500 885 590 865 680 820 Z"/>
      </svg>

      <div class="cover-illustration" role="img" aria-label="Pale gold line illustration of a winged figure reaching toward a bursting firework starburst with scattered sparks"></div>

      <div class="title-block">
        <h1 class="book-title">Lantern over<br>the Harbor</h1>
        <p class="book-subtitle">A Widening Passage for Writers</p>
        <p class="book-author">Dorothea Quillbrake</p>
      </div>
    </section>
  </main>
</body>
</html>
```